New lease of life for a tired Country Pub menu, QLD

I need to refresh my menus with updated prices. The menus need to be A4 (the menus are laminated and handed out over the bar. I'd like to include our logo. I will upload our existing menus as well as the new prices. The design should be humble yet stylish if that's ok, please

Target Market(s)

Locals, travellers and workers

Industry/Entity Type

Hospitality, Quintessential Country pub

Font styles to use
Sans Serif

Colors

Designer to choose colors to be used in the design.

Requirements
Must have
• as we run different menus on different nights
Nice to have
• our logo

```html
<!DOCTYPE html>
<html lang="en">
<head>
<meta charset="utf-8">
<title>Hotel Calloway – Lunch Menu</title>
<link href="https://fonts.googleapis.com/css2?family=Titan+One&family=Cutive+Mono&display=swap" rel="stylesheet">
<style>
  :root {
    --paper: #ffffff;
    --stone: #bdbdbd;
    --slate: #474747;
    --band: #6e6e6e;
    --ink: #111111;
    --chalk: #f2f2f2;
  }
  * { margin: 0; padding: 0; box-sizing: border-box; }
  html, body { width: 845px; height: 1200px; overflow: hidden; background: var(--paper); }
  .menu {
    position: relative; width: 845px; height: 1200px; overflow: hidden;
    background: linear-gradient(to bottom, var(--paper) 0 567px, var(--stone) 567px 100%);
    font-family: "Cutive Mono", "Courier New", monospace;
  }
  .title-band {
    position: absolute; left: 287px; top: 26px; width: 558px; height: 130px;
    background: var(--band); border-radius: 32px 0 0 32px;
  }
  .title {
    position: absolute; left: 50px; top: 30px;
    font-family: "Titan One", sans-serif; font-weight: 400;
    font-size: 59px; line-height: 1; color: var(--paper); letter-spacing: 1px;
    white-space: nowrap;
  }
  .feature-panel {
    position: absolute; left: 23px; top: 99px; width: 785px; height: 587px;
    background: var(--slate); border-radius: 31px;
  }
  .venue-card {
    position: absolute; left: 56px; top: 38px; width: 200px; height: 120px;
    background: var(--paper); border-radius: 14px;
    display: flex; align-items: center; justify-content: center; gap: 8px;
  }
  .venue-dot { width: 10px; height: 10px; border-radius: 50%; background: var(--ink); }
  .venue-name {
    font-family: "Cutive Mono", "Courier New", monospace; font-size: 17px;
    color: var(--ink); white-space: nowrap;
  }
  .members-label {
    position: absolute; left: 672px; top: 188px;
    font-family: "Titan One", sans-serif; font-size: 16px; color: var(--chalk);
  }
  .dish { position: absolute; left: 66px; width: 720px; }
  .dish-name {
    font-family: "Titan One", sans-serif; font-size: 22.3px; line-height: 1;
    letter-spacing: .3px; text-transform: uppercase; font-weight: 400;
  }
  .dish-desc { font-size: 16.2px; line-height: 25.6px; width: 450px; }
  .price { position: absolute; font-size: 16.2px; line-height: 25.6px; }
  .on-dark { color: var(--chalk); }
  .on-light { color: var(--ink); }
  .on-light .dish-name { font-size: 22px; }
  .extra { position: absolute; left: 271px; font-size: 16.2px; line-height: 25.6px; color: var(--ink); }
  .inline-desc { position: absolute; left: 184px; font-size: 16.2px; line-height: 25.6px; color: var(--ink); }
</style>
</head>
<body>
<main class="menu">
  <div class="feature-panel"></div>
  <div class="title-band"><h1 class="title">LUNCH MENU</h1></div>
  <div class="venue-card"><span class="venue-dot"></span><span class="venue-name">Hotel Calloway</span></div>

  <div class="members-label">Members</div>

  <section class="dish on-dark" style="top:187px">
    <h2 class="dish-name">Chicken Burger</h2>
    <p class="dish-desc" style="margin-top:8px">Fried Marlow Butchery crumbed chicken thigh, cheese, tomato, spanish onion with aioli</p>
  </section>
  <span class="price on-dark" style="left:552px;top:227px">$19.99</span>
  <span class="price on-dark" style="left:686px;top:227px">$18.99</span>

  <section class="dish on-dark" style="top:292px">
    <h2 class="dish-name">Beef Burger</h2>
    <p class="dish-desc" style="margin-top:8px">Grilled angus beef patty, lettuce, cheese, beetroot, tomato, spanish onion, pickles, caramelised onion with aioli</p>
  </section>
  <span class="price on-dark" style="left:552px;top:323px">$19.99</span>
  <span class="price on-dark" style="left:686px;top:323px">$18.99</span>

  <section class="dish on-dark" style="top:424px">
    <h2 class="dish-name">Steak Burger</h2>
    <p class="dish-desc" style="margin-top:17px">Grilled Marlow Butchery rib fillet, lettuce, tomato, spanish onion, beetroot, cheese, caramelised onion with bbq sauce</p>
  </section>
  <span class="price on-dark" style="left:552px;top:464px">$21</span>
  <span class="price on-dark" style="left:706px;top:464px">$19</span>

  <section class="dish on-dark" style="top:565px">
    <h2 class="dish-name">Barramundi Burger</h2>
    <p class="dish-desc" style="margin-top:16px;width:440px">Southern fried barramundi, lettuce, coleslaw with homemade dill and chives aioli</p>
  </section>
  <span class="price on-dark" style="left:552px;top:598px">$18.99</span>
  <span class="price on-dark" style="left:686px;top:598px">$17.99</span>

  <section class="dish on-light" style="top:707px">
    <h2 class="dish-name">Ceasar Salad</h2>
    <p class="dish-desc" style="margin-top:15px">Cos lettuce, croutons, parmesan cheese, boiled egg, caesar dressing</p>
  </section>
  <span class="price on-light" style="left:549px;top:746px">$17.99</span>
  <span class="price on-light" style="left:684px;top:746px">$16.99</span>
  <span class="extra" style="top:794px">ADD CHICKEN</span>
  <span class="price on-light" style="left:549px;top:797px">$21</span>
  <span class="price on-light" style="left:703px;top:797px">$20</span>
  <span class="extra" style="top:833px">ADD CALAMARI</span>
  <span class="price on-light" style="left:549px;top:833px">$22.50</span>
  <span class="price on-light" style="left:684px;top:833px">$21.50</span>

  <section class="dish on-light" style="top:894px">
    <h2 class="dish-name">Wrap It</h2>
  </section>
  <span class="inline-desc" style="top:893px">Chicken caesar salad wrap</span>
  <span class="price on-light" style="left:549px;top:896px">$19</span>
  <span class="price on-light" style="left:703px;top:896px">$18</span>

  <section class="dish on-light" style="top:949px">
    <h2 class="dish-name">Honey Mustard Chicken Salad</h2>
    <p class="dish-desc" style="margin-top:15px;width:480px">Mesclun mix, continental cucumber, cherry tomato, spanish onion, crispy chicken tenders (breast)</p>
  </section>
  <span class="price on-light" style="left:549px;top:985px">$19</span>
  <span class="price on-light" style="left:703px;top:985px">$18</span>

  <section class="dish on-light" style="top:1063px">
    <h2 class="dish-name">Bangin Burrito</h2>
    <p class="dish-desc" style="margin-top:8px">Minced beef, sliced beef sausage, rice, tomato puree, herbs</p>
  </section>
  <span class="price on-light" style="left:549px;top:1091px">$21</span>
  <span class="price on-light" style="left:703px;top:1091px">$20</span>
</main>
</body>
</html>
```